We need a design for our retail display and for our stockist's retail display.
Our product is fresh corn tortillas. These can be used to make tacos, quesadillas, tortilla chips and tostadas.
We want the table talker to use our brand style (see our website) and show the tortillas versatility.
verdel-foods.co.uk
It should also have a space for our stockists to write in a blank space under the heading "Our fresh tortillas are delivered every....[blank space]"
The table talker should be 75mm tall x 150mm wide. This will also have a 25mm self adhesive flap at the top which can be blank or the same colour as the background.
Please feel free to use any files from our website as well as illustrations attached.
Customers in high end shops and delis
food and drink

```html
<!DOCTYPE html>
<html lang="en">
<head>
<meta charset="utf-8">
<title>Verdel Foods – Table Talker</title>
<link rel="stylesheet" href="https://fonts.googleapis.com/css2?family=Lilita+One&family=Montserrat:wght@400;700;800&family=Poppins:wght@500;600&display=swap">
<style>
  :root {
    --navy: #1b2a43;
    --yellow: #e2bd2c;
    --bright-yellow: #f2e21e;
    --canvas: #eef0ec;
    --white: #ffffff;
  }
  * { margin: 0; padding: 0; box-sizing: border-box; }
  html, body { width: 1200px; height: 1200px; overflow: hidden; background: var(--canvas); }
  .talker {
    position: absolute; left: 0; top: 298px;
    width: 1200px; height: 603px; overflow: hidden;
    background: var(--yellow);
  }
  .talker__shapes { position: absolute; inset: 0; }
  .brand {
    position: absolute; left: 520px; top: 30px;
    width: 160px; height: 160px; border-radius: 50%;
    background: var(--navy);
    display: flex; align-items: center; justify-content: center;
  }
  .brand__name {
    font-family: "Lilita One", sans-serif; font-size: 40px;
    color: var(--bright-yellow);
  }
  .uses {
    position: absolute; right: 40px; top: 46px; width: 250px;
    text-align: right; color: var(--navy);
    font-family: "Montserrat", sans-serif;
  }
  .uses__label { font-weight: 400; font-size: 15px; letter-spacing: 3px; }
  .uses__list { list-style: none; font-weight: 800; font-size: 19px; letter-spacing: 2px; line-height: 1.3; margin-top: 4px; }
  .headline {
    position: absolute; left: 0; width: 100%; top: 204px;
    text-align: center;
    font-family: "Lilita One", sans-serif; font-size: 86px; line-height: 1;
    color: var(--navy); letter-spacing: 1px;
    text-shadow: 3px 3px 0 var(--bright-yellow);
  }
  .subline {
    position: absolute; left: 0; width: 100%; top: 296px;
    text-align: center;
    font-family: "Montserrat", sans-serif; font-weight: 400; font-size: 30px;
    letter-spacing: 5px; color: var(--navy); line-height: 1;
  }
  .ingredients-box {
    position: absolute; left: 186px; top: 341px; width: 828px; height: 75px;
    background: var(--white); border: 3px solid var(--navy);
    display: flex; align-items: center; justify-content: center;
    font-family: "Montserrat", sans-serif; font-weight: 800; font-size: 44px;
    letter-spacing: 11px; color: var(--navy);
  }
  .open-box {
    position: absolute; left: 454px; top: 426px; width: 293px; height: 46px;
    background: var(--navy);
    display: flex; align-items: center; justify-content: center; gap: 12px;
    font-family: "Montserrat", sans-serif; font-weight: 800; font-size: 32px;
    color: var(--white);
  }
  .open-box__accent { color: var(--bright-yellow); }
  .product-strip {
    position: absolute; left: 0; top: 496px; width: 826px; height: 34px;
    background: linear-gradient(90deg, var(--bright-yellow) 0%, rgba(242,226,30,0.6) 100%);
    display: flex; align-items: center; padding-left: 28px;
    font-family: "Poppins", sans-serif; font-weight: 500; font-size: 17px;
    color: var(--navy); white-space: nowrap;
  }
  .delivery {
    position: absolute; left: 28px; top: 546px;
    display: flex; align-items: center; gap: 12px;
    font-family: "Poppins", sans-serif; font-weight: 600; font-size: 18px;
    color: var(--navy); white-space: nowrap;
  }
  .delivery__blank {
    width: 260px; height: 38px;
    background: var(--white); border: 2px solid var(--navy);
  }
</style>
</head>
<body>
  <section class="talker">
    <svg class="talker__shapes" width="1200" height="603" viewBox="0 0 1200 603">
      <defs>
        <linearGradient id="photo-tones" x1="0" y1="0" x2="1" y2="1">
          <stop offset="0" stop-color="#8a7a60"/>
          <stop offset="0.45" stop-color="#b23a22"/>
          <stop offset="1" stop-color="#c9a36b"/>
        </linearGradient>
        <linearGradient id="pattern-tones" x1="0" y1="0" x2="1" y2="1">
          <stop offset="0" stop-color="#1d2a66"/>
          <stop offset="1" stop-color="#2f4f91"/>
        </linearGradient>
      </defs>
      <polygon points="0,0 363,0 0,283" fill="url(#photo-tones)" role="img" aria-label="Photo of salsa in a white ramekin beside corn tortilla tacos"/>
      <polygon points="1200,236 1200,603 739,603" fill="url(#pattern-tones)" role="img" aria-label="Blue decorative folk pattern of leaves and dots"/>
    </svg>

    <div class="brand"><span class="brand__name">Verdel</span></div>

    <div class="uses">
      <p class="uses__label">PERFECT FOR</p>
      <ul class="uses__list">
        <li>TACOS</li>
        <li>QUESADILLAS</li>
        <li>TORTILLA CHIPS</li>
        <li>TOSTADAS</li>
      </ul>
    </div>

    <h1 class="headline">FRESH CORN TORTILLAS</h1>
    <p class="subline">and other</p>
    <div class="ingredients-box">MEXICAN INGREDIENTS</div>
    <div class="open-box"><span>OPEN</span><span class="open-box__accent">TODAY</span></div>
    <div class="product-strip">DRIED CHILLIS | MASA HARINA | HOT SAUCES | TORTILLA PRESSES | TORTILLA WARMERS</div>
    <div class="delivery">
      <span>Our fresh tortillas are delivered every…</span>
      <span class="delivery__blank" aria-label="Space for stockist to write delivery day"></span>
    </div>
  </section>
</body>
</html>
```